Postcard Design

Marlow Painting-all types of painting and staining-house,deck and roof powerwashing-stone and masonry sealing-
30 years in business-licensed and insured
Ray Pettibone
pettiboneworks@brushmail.example
9145820731

Industry/Entity Type

Painting

```html
<!DOCTYPE html>
<html lang="en">
<head>
<meta charset="utf-8">
<title>Marlow Painting – Postcard</title>
<link rel="stylesheet" href="https://fonts.googleapis.com/css2?family=Exo+2:wght@400;500&family=Open+Sans:wght@400;600;700;800&display=swap">
<style>
  :root {
    --stage: #3a3a3a;
    --purple: #5b3f7c;
    --purple-deep: #3f2a5a;
    --purple-light: #8a6aad;
    --gold: #e3ad2a;
    --gold-light: #f6d35a;
    --yellow: #f2e21c;
    --green: #6cbf3a;
    --ink: #1c1c1c;
    --white: #ffffff;
    --paper-grey: #f0f0f0;
    --line-grey: #e2e2e2;
  }
  * { box-sizing: border-box; margin: 0; padding: 0; }
  html, body { width: 1200px; height: 887px; overflow: hidden; background: var(--stage); }
  body { position: relative; font-family: "Open Sans", Arial, sans-serif; }

  /* ---------- Front ---------- */
  .front {
    position: absolute; left: 48px; top: 32px;
    width: 546px; height: 422px;
    background: var(--white); overflow: hidden;
    box-shadow: 0 4px 14px rgba(0,0,0,.45);
  }
  .front__photo {
    position: absolute; left: 0; top: 118px; width: 235px; height: 260px;
    background: linear-gradient(180deg, #c9d3dc 0%, #b8b3aa 45%, #8f9a78 80%, #5f7d3c 100%);
  }
  .front__panel { position: absolute; inset: 0; }
  .front__brand {
    position: absolute; left: 18px; top: 50px; width: 190px;
    font-family: "Exo 2", Arial, sans-serif; font-weight: 500;
    font-size: 26px; line-height: 1.05; color: var(--purple);
    text-transform: uppercase;
  }
  .front__title {
    position: absolute; left: 240px; top: 24px;
    font-family: "Exo 2", Arial, sans-serif; font-weight: 400;
    font-size: 29px; color: var(--white); letter-spacing: .5px;
  }
  .front__intro {
    position: absolute; left: 242px; top: 60px; width: 215px;
    font-size: 10.5px; line-height: 1.3; color: var(--white);
  }
  .front__pour {
    position: absolute; left: 462px; top: 70px; width: 84px; height: 300px;
    background: linear-gradient(180deg, #cfcfcf 0%, #8c8c8c 22%, var(--gold-light) 30%, var(--gold) 70%, #c98b12 100%);
    border-radius: 40px 0 0 0;
  }
  .services { position: absolute; left: 242px; top: 170px; display: flex; gap: 10px; color: var(--white); }
  .services__label { font-weight: 800; line-height: 1; }
  .services__label b { display: block; font-size: 22px; }
  .services__label span { display: block; font-size: 11.5px; }
  .services__list { list-style: none; font-size: 11px; font-weight: 600; line-height: 1.3; width: 170px; }
  .services__list li { position: relative; padding-left: 16px; }
  .services__list li::before { content: "●"; position: absolute; left: 0; font-size: 8px; top: 2px; }

  .badge {
    position: absolute; height: 24px; display: flex; align-items: center;
    background: linear-gradient(180deg, var(--gold-light), var(--gold));
    border-radius: 4px; padding-left: 40px; font-size: 13.5px; color: var(--ink);
    box-shadow: 0 1px 3px rgba(0,0,0,.4);
  }
  .badge b { font-weight: 800; margin-right: 4px; }
  .badge svg { position: absolute; left: 0; top: -4px; }
  .badge--years { left: 254px; top: 279px; width: 200px; }
  .badge--licence { left: 324px; top: 314px; width: 198px; }

  .front__name {
    position: absolute; left: 0; top: 347px; width: 225px; height: 22px;
    background: var(--green); color: var(--white);
    font-weight: 700; font-size: 14px; letter-spacing: 1.5px; padding-left: 40px; line-height: 22px;
    clip-path: polygon(0 0, 92% 0, 100% 100%, 0 100%);
  }
  .front__contact {
    position: absolute; left: 0; top: 369px; width: 100%; height: 28px;
    background: linear-gradient(180deg, var(--gold-light), var(--gold));
    display: flex; align-items: center; padding-left: 40px;
  }
  .front__phone { display: flex; align-items: center; gap: 8px; font-weight: 800; font-size: 20px; letter-spacing: 1px; color: var(--ink); }
  .front__email { margin-left: auto; margin-right: 12px; display: flex; align-items: center; gap: 6px; font-size: 12.5px; color: var(--ink); }
  .front__base { position: absolute; left: 0; bottom: 0; width: 100%; height: 25px; }

  /* ---------- Back ---------- */
  .back {
    position: absolute; left: 615px; top: 440px;
    width: 543px; height: 416px; background: var(--white);
    box-shadow: 0 4px 14px rgba(0,0,0,.45);
  }
  .back__brandzone {
    position: absolute; left: 0; top: 0; width: 263px; height: 154px;
    background: radial-gradient(circle at 50% 45%, var(--white), var(--paper-grey));
    display: flex; align-items: center; justify-content: center;
  }
  .back__brand {
    font-family: "Exo 2", Arial, sans-serif; font-weight: 500; font-size: 26px;
    color: var(--purple); text-transform: uppercase; text-align: center; line-height: 1.05;
  }
  .back__rule {
    position: absolute; left: 0; top: 154px; width: 263px; height: 4px;
    background: linear-gradient(90deg, var(--purple), #d23b7a, var(--gold), #35a3d8, var(--purple));
  }
  .back__panel {
    position: absolute; left: 0; top: 158px; width: 263px; height: 190px;
    background: linear-gradient(180deg, var(--purple) 0%, var(--purple-deep) 100%);
    color: var(--white); padding: 10px 0 0 16px;
  }
  .back__title { font-family: "Exo 2", Arial, sans-serif; font-size: 22px; letter-spacing: .3px; }
  .back__heading { margin-top: 14px; font-weight: 700; font-size: 20px; }
  .back__list { list-style: none; font-size: 9.5px; line-height: 1.15; margin-top: 2px; }
  .back__list li::before { content: "● "; font-size: 7px; margin-right: 6px; }
  .back__phone { margin-top: 20px; display: flex; align-items: center; gap: 10px; font-weight: 800; font-size: 25px; letter-spacing: 1.5px; }
  .back__stamp { position: absolute; left: 450px; top: 12px; width: 78px; height: 88px; background: var(--paper-grey); }
  .back__lines { position: absolute; left: 305px; top: 247px; width: 220px; }
  .back__lines span { display: block; height: 1px; background: var(--line-grey); margin-bottom: 21px; }
</style>
</head>
<body>

<section class="front" aria-label="Postcard front">
  <div class="front__photo" role="img" aria-label="Photo of a two-storey brick and siding house with a white balcony"></div>

  <svg class="front__panel" width="546" height="422" viewBox="0 0 546 422" aria-hidden="true">
    <defs>
      <radialGradient id="panelGlow" cx="0.55" cy="0.45" r="0.7">
        <stop offset="0" stop-color="#7a5a9e"/>
        <stop offset="1" stop-color="#4a3068"/>
      </radialGradient>
    </defs>
    <path d="M214 0 H546 V370 H222 C200 270 205 120 214 0 Z" fill="#8a6aad"/>
    <path d="M224 0 H546 V370 H232 C212 270 215 120 224 0 Z" fill="url(#panelGlow)"/>
  </svg>

  <div class="front__brand">Marlow Painting</div>
  <h1 class="front__title">MARLOW PAINTING</h1>
  <p class="front__intro">Professional Home Services specializes in exterior, residential and commercial painting projects</p>

  <div class="front__pour" role="img" aria-label="Paint can pouring golden yellow paint"></div>

  <div class="services">
    <div class="services__label"><b>OUR</b><span>SERVICE</span></div>
    <ul class="services__list">
      <li>all types of painting and staining</li>
      <li>house,deck and roof powerwashing</li>
      <li>stone and masonry sealing</li>
    </ul>
  </div>

  <div class="badge badge--years">
    <svg width="32" height="32" viewBox="0 0 32 32" aria-hidden="true"><circle cx="16" cy="16" r="14" fill="#222" stroke="#f6d35a" stroke-width="3"/><path d="M10 16 l4 5 l8 -10" fill="none" stroke="#f6d35a" stroke-width="3"/></svg>
    <b>30 years</b> in business
  </div>
  <div class="badge badge--licence">
    <svg width="32" height="32" viewBox="0 0 32 32" aria-hidden="true"><circle cx="16" cy="16" r="14" fill="#222" stroke="#f6d35a" stroke-width="3"/><path d="M10 16 l4 5 l8 -10" fill="none" stroke="#f6d35a" stroke-width="3"/></svg>
    <b>Licensed</b> and <b style="margin-left:4px">Insured</b>
  </div>

  <div class="front__name">Ray Pettibone</div>
  <div class="front__contact">
    <span class="front__phone">
      <svg width="18" height="18" viewBox="0 0 20 20" aria-hidden="true"><circle cx="10" cy="10" r="9" fill="none" stroke="#1c1c1c" stroke-width="1.5"/><path d="M7 5 c-2 2 0 7 5 10 l2 -2 l-2 -2 l-1 1 c-1 -1 -3 -3 -3 -4 l1 -1 l-2 -2 z" fill="#1c1c1c"/></svg>
      9145820731
    </span>
    <span class="front__email">
      <svg width="14" height="10" viewBox="0 0 14 10" aria-hidden="true"><rect x="0.5" y="0.5" width="13" height="9" fill="none" stroke="#1c1c1c"/><path d="M0.5 0.5 L7 6 L13.5 0.5" fill="none" stroke="#1c1c1c"/></svg>
      pettiboneworks@brushmail.example
    </span>
  </div>
  <svg class="front__base" viewBox="0 0 546 25" preserveAspectRatio="none" aria-hidden="true">
    <rect width="546" height="25" fill="#ffffff"/>
    <path d="M150 0 H546 V6 C420 10 300 18 170 25 Z" fill="#f2e21c"/>
    <path d="M0 0 H150 L170 25 H0 Z" fill="#7f9a5a"/>
  </svg>
</section>

<section class="back" aria-label="Postcard back">
  <div class="back__brandzone"><div class="back__brand">Marlow<br>Painting</div></div>
  <div class="back__rule"></div>
  <div class="back__panel">
    <h2 class="back__title">MARLOW PAINTING</h2>
    <h3 class="back__heading">OUR SERVICE</h3>
    <ul class="back__list">
      <li>all types of painting and staining</li>
      <li>house,deck and roof powerwashing</li>
      <li>stone and masonry sealing</li>
    </ul>
    <div class="back__phone">
      <svg width="24" height="24" viewBox="0 0 20 20" aria-hidden="true"><circle cx="10" cy="10" r="9" fill="none" stroke="#fff" stroke-width="1.5"/><path d="M7 5 c-2 2 0 7 5 10 l2 -2 l-2 -2 l-1 1 c-1 -1 -3 -3 -3 -4 l1 -1 l-2 -2 z" fill="#fff"/></svg>
      9145820731
    </div>
  </div>
  <div class="back__stamp" aria-label="Stamp area"></div>
  <div class="back__lines" aria-label="Address lines"><span></span><span></span><span></span><span></span></div>
</section>

</body>
</html>
```